Beauty & Wellness business needs a flyer to describe a multitude of therapy

I would like a flyer to represent my company. i would like it to have the form of a pamphlet 6 pages. The flyer should be in french if possible, but english also is okay. I'll upload a word file that illustrate what i would like, but it can be of course other images, this is just an example. And the text includes all the services we provide, some small description might be added if you think it's worth it from design point of view.
Target Market(s)
The market is seasonal. it's mostly winter for skiers, so wealthy and sporty people, and attentive to nature. But i also want to promote the brand for locals all year long, with reasonable pricing.
Industry/Entity Type
Wellness & aesthetics
Look and feel

```html
<!DOCTYPE html>
<html lang="fr">
<head>
<meta charset="utf-8">
<title>Lumea Studio – Beauty &amp; Therapy brochure</title>
<link href="https://fonts.googleapis.com/css2?family=DM+Serif+Display&family=Open+Sans:wght@400;600&display=swap" rel="stylesheet">
<style>
  :root {
    --plum: #6b1d5c;
    --plum-deep: #561349;
    --blush: #f4ddd6;
    --blush-soft: #fbeeea;
    --rose: #e9c3bb;
    --gold: #d8b596;
    --ink: #4a3a44;
    --white: #ffffff;
    --stage: #dcdad7;
    --serif: "DM Serif Display", Georgia, serif;
    --sans: "Open Sans", Arial, sans-serif;
  }
  * { box-sizing: border-box; margin: 0; padding: 0; }
  html, body { width: 1200px; height: 2400px; overflow: hidden; }
  body { background: var(--stage); font-family: var(--sans); color: var(--ink); position: relative; }

  .spread {
    position: absolute; left: 30px; width: 1140px; height: 820px;
    display: flex; box-shadow: 0 10px 30px rgba(60, 40, 50, .18);
  }
  .spread--outside { top: 300px; }
  .spread--inside { top: 1280px; }

  .panel { position: relative; width: 380px; height: 820px; overflow: hidden; background: var(--white); }
  .panel + .panel { border-left: 1px solid rgba(0,0,0,.06); }
  .layer { position: absolute; left: 0; top: 0; width: 380px; height: 820px; }

  .photo { position: absolute; }
  .photo--round { border-radius: 50%; border: 5px solid var(--white); box-shadow: 0 3px 10px rgba(0,0,0,.12); }

  .brand { position: absolute; left: 0; width: 100%; display: flex; flex-direction: column; align-items: center; gap: 10px; }
  .brand__mark { width: 46px; height: 46px; border-radius: 50%; border: 2px solid var(--plum); }
  .brand__name { font-family: var(--serif); color: var(--plum); font-size: 24px; letter-spacing: 3px; text-transform: uppercase; }

  .pill {
    display: inline-block; font-family: var(--serif); color: var(--plum);
    background: var(--blush); border-radius: 20px; padding: 5px 20px; font-size: 19px;
  }
  .pill--on-plum { background: var(--blush-soft); }

  .tagline { font-family: var(--serif); color: var(--white); font-size: 38px; }
  .tagline--plum { color: var(--plum); }
  .web { font-size: 16px; color: var(--white); letter-spacing: .5px; }
  .web-pill { display: inline-block; background: var(--white); color: var(--plum); border-radius: 18px; padding: 6px 22px; font-size: 15px; font-weight: 600; }
  .web-pill--plum { background: var(--plum); color: var(--white); }

  .body-copy { font-size: 12.5px; line-height: 1.6; }

  /* Welcome panel */
  .welcome__head { position: absolute; top: 34px; left: 28px; }
  .welcome__text { position: absolute; top: 90px; left: 28px; right: 28px; }
  .welcome__text p + p { margin-top: 12px; }
  .welcome__band { position: absolute; top: 640px; left: 28px; right: 28px; color: var(--white); }

  /* Contact panel */
  .contact { background: linear-gradient(180deg, var(--blush-soft), var(--blush)); }
  .contact__intro { position: absolute; top: 160px; left: 30px; right: 30px; text-align: center; font-family: var(--serif); color: var(--plum); font-size: 21px; line-height: 1.25; }
  .contact__list { position: absolute; top: 250px; left: 60px; right: 30px; list-style: none; color: var(--plum); }
  .contact__list li { display: flex; align-items: center; gap: 10px; margin-bottom: 12px; font-size: 15px; }
  .contact__list .phone { font-size: 21px; font-weight: 600; }
  .contact__note { display: block; margin: 4px 0 6px; font-size: 14px; }
  .icon { width: 24px; height: 24px; flex: none; }
  .contact__address { position: absolute; top: 690px; left: 0; width: 100%; text-align: center; color: var(--white); font-size: 17px; letter-spacing: 1px; line-height: 1.35; text-transform: uppercase; }
  .contact__web { position: absolute; top: 758px; left: 0; width: 100%; text-align: center; }

  /* Cover */
  .cover__tag { position: absolute; top: 690px; left: 0; width: 100%; text-align: center; }
  .cover__web { position: absolute; top: 752px; left: 0; width: 100%; text-align: center; }

  /* Service lists */
  .service { position: absolute; left: 28px; right: 24px; }
  .service__list { list-style: none; margin-top: 14px; }
  .service__list li { position: relative; padding-left: 26px; font-size: 15px; line-height: 1.85; }
  .service__list li::before {
    content: ""; position: absolute; left: 2px; top: 8px; width: 12px; height: 12px;
    border: 1.5px solid currentColor; border-radius: 50%;
  }
  .service__list li::after {
    content: ""; position: absolute; left: 6px; top: 12px; width: 3px; height: 3px;
    border-top: 1.5px solid currentColor; border-right: 1.5px solid currentColor; transform: rotate(45deg);
  }
  .service--light { color: var(--white); }
  .service--dark { color: var(--ink); }
  .service__extra { margin-top: 26px; font-family: var(--serif); color: var(--white); font-size: 21px; line-height: 1.3; }

  .massage__foot { position: absolute; top: 700px; left: 0; width: 100%; text-align: center; }
  .massage__foot .web-pill { margin-top: 8px; }
</style>
</head>
<body>

<!-- Outside spread -->
<section class="spread spread--outside">

  <article class="panel welcome">
    <svg class="layer" viewBox="0 0 380 820" aria-hidden="true">
      <path d="M0 470 Q190 420 380 480 V820 H0 Z" fill="var(--blush)"/>
      <path d="M0 600 Q190 540 380 580 V820 H0 Z" fill="var(--plum)"/>
    </svg>
    <div class="welcome__head"><span class="pill">Welcome to Lumea Studio</span></div>
    <div class="welcome__text body-copy">
      <p>We are delighted to welcome you into a calm space devoted to face and body care. Our team combines gentle techniques, natural products and attentive advice so that every visit leaves you rested, radiant and ready for the mountains.</p>
      <p>Whether you ski all winter or live here all year, we tailor each treatment to your needs with fair prices and warm, personal attention.</p>
    </div>
    <div class="photo photo--round" role="img" aria-label="Photo of smooth, waxed legs" style="left:30px;top:440px;width:130px;height:130px;background:linear-gradient(135deg,#c9dbe0,#e8cfc0);"></div>
    <div class="photo photo--round" role="img" aria-label="Photo of a woman receiving a facial treatment" style="left:175px;top:430px;width:120px;height:120px;background:linear-gradient(135deg,#f0dcd2,#c79d88);"></div>
    <p class="welcome__band body-copy">Take a moment for yourself. Book a massage, a facial or a simple pause, and leave feeling light, confident and beautifully cared for.</p>
  </article>

  <article class="panel contact">
    <svg class="layer" viewBox="0 0 380 820" aria-hidden="true">
      <path d="M0 640 Q190 600 380 650 V820 H0 Z" fill="var(--plum)"/>
    </svg>
    <div class="brand" style="top:40px">
      <span class="brand__mark"></span>
      <span class="brand__name">Lumea Studio</span>
    </div>
    <p class="contact__intro">Pour prendre un rendez-vous<br>ou une consultation gratuite:</p>
    <ul class="contact__list">
      <li class="phone">
        <svg class="icon" viewBox="0 0 24 24" aria-hidden="true"><circle cx="12" cy="12" r="12" fill="var(--plum)"/><path d="M8.5 6.5l2 2-1.2 1.6c.7 1.6 2 2.9 3.6 3.6l1.6-1.2 2 2-1.3 1.8c-4.6-.5-8.2-4.1-8.7-8.7z" fill="#fff"/></svg>
        +41 79 000 1234
      </li>
      <li>
        <svg class="icon" viewBox="0 0 24 24" aria-hidden="true"><circle cx="12" cy="12" r="12" fill="var(--plum)"/><rect x="6.5" y="8" width="11" height="8" rx="1" fill="none" stroke="#fff" stroke-width="1.4"/><path d="M6.8 8.5l5.2 4 5.2-4" fill="none" stroke="#fff" stroke-width="1.4"/></svg>
        contact@lumea-studio.ch
      </li>
      <li style="display:block"><span class="contact__note">For more information, visit us at:</span></li>
      <li>
        <svg class="icon" viewBox="0 0 24 24" aria-hidden="true"><circle cx="12" cy="12" r="12" fill="var(--plum)"/><path d="M12 5.5a4.2 4.2 0 0 0-4.2 4.2c0 3.1 4.2 8 4.2 8s4.2-4.9 4.2-8A4.2 4.2 0 0 0 12 5.5z" fill="#fff"/><circle cx="12" cy="9.7" r="1.6" fill="var(--plum)"/></svg>
        www.lumea-studio.ch
      </li>
    </ul>
    <div class="photo photo--round" role="img" aria-label="Street map showing the studio location" style="left:20px;top:480px;width:160px;height:160px;background:linear-gradient(135deg,#f4f4f6,#dfe3ea);"></div>
    <p class="contact__address">Chemin des Alpes 12,<br>Valmont, Suisse</p>
    <div class="contact__web"><span class="web-pill">www.lumea-studio.ch</span></div>
  </article>

  <article class="panel cover">
    <div class="brand" style="top:40px">
      <span class="brand__mark"></span>
      <span class="brand__name">Lumea Studio</span>
    </div>
    <svg class="layer" viewBox="0 0 380 820" aria-hidden="true">
      <path d="M0 170 Q190 140 380 190 V600 H0 Z" fill="var(--blush-soft)"/>
      <path d="M0 175 Q190 145 380 195" fill="none" stroke="var(--gold)" stroke-width="1.5"/>
    </svg>
    <div class="photo" role="img" aria-label="Photo of three smiling women in nude-toned dresses" style="left:20px;top:200px;width:360px;height:440px;background:linear-gradient(160deg,#f3e6df 0%,#d9b8a4 50%,#a97a62 100%);"></div>
    <svg class="layer" viewBox="0 0 380 820" aria-hidden="true">
      <path d="M0 600 Q190 560 380 600 V820 H0 Z" fill="var(--blush)"/>
      <path d="M0 640 Q190 590 380 630 V820 H0 Z" fill="var(--plum)"/>
    </svg>
    <div class="cover__tag"><span class="tagline">Beauty &amp; Therapy</span></div>
    <div class="cover__web"><span class="web">www.lumea-studio.ch</span></div>
  </article>
</section>

<!-- Inside spread -->
<section class="spread spread--inside">

  <article class="panel face">
    <svg class="layer" viewBox="0 0 380 820" aria-hidden="true">
      <path d="M0 0 H380 V540 Q190 600 0 560 Z" fill="var(--plum)"/>
      <path d="M0 560 Q190 600 380 540 V560 Q190 620 0 580 Z" fill="var(--blush)"/>
    </svg>
    <div class="service service--light" style="top:40px">
      <span class="pill pill--on-plum">Nos traitements du visage</span>
      <ul class="service__list">
        <li>Soin du visage classique</li>
        <li>Fils de collagènes</li>
        <li>Thérapie au plâtre</li>
        <li>Plasma Lift</li>
        <li>Chromothérapie</li>
        <li>Aromathérapie</li>
        <li>Needling</li>
      </ul>
      <p class="service__extra">Épilation masculine et féminin<br>Design des sourcils</p>
    </div>
    <div class="photo" role="img" aria-label="Portrait of a woman with glowing skin touching her face" style="left:0;top:590px;width:380px;height:230px;background:linear-gradient(180deg,#f1e6e1,#d9c0b3);"></div>
    <div class="photo photo--round" role="img" aria-label="Photo of an eyebrow shaping treatment" style="left:250px;top:500px;width:100px;height:100px;background:linear-gradient(135deg,#f2ded6,#c9a08d);"></div>
  </article>

  <article class="panel massage">
    <svg class="layer" viewBox="0 0 380 820" aria-hidden="true">
      <path d="M0 640 Q190 600 380 650 V820 H0 Z" fill="var(--blush)"/>
    </svg>
    <div class="service service--dark" style="top:40px;left:40px">
      <span class="pill">Nos massages maison</span>
      <ul class="service__list">
        <li>Sportif</li>
        <li>Pierre chaude</li>
        <li>Ayurvédique Pindas</li>
        <li>Guasha</li>
        <li>Bambou</li>
        <li>Drainage lymphatique</li>
        <li>Pour femmes enceintes</li>
        <li>Réflexologie</li>
        <li>Relaxant</li>
        <li>Shiatsu</li>
        <li>Deep tissue</li>
        <li>Meso Cellulita</li>
      </ul>
    </div>
    <div class="photo photo--round" role="img" aria-label="Photo of a back massage" style="left:30px;top:560px;width:110px;height:110px;background:linear-gradient(135deg,#e8cbb6,#a97c63);"></div>
    <div class="photo photo--round" role="img" aria-label="Photo of a woman relaxing during a facial" style="left:135px;top:540px;width:120px;height:120px;background:linear-gradient(135deg,#f3e4dc,#c9a895);"></div>
    <div class="photo photo--round" role="img" aria-label="Photo of spa stones and towels" style="left:250px;top:560px;width:110px;height:110px;background:linear-gradient(135deg,#efe7dd,#b89b84);"></div>
    <div class="massage__foot">
      <span class="tagline tagline--plum">Beauty &amp; Therapy</span><br>
      <span class="web-pill web-pill--plum">www.lumea-studio.ch</span>
    </div>
  </article>

  <article class="panel nails">
    <div class="photo" role="img" aria-label="Photo of a relaxing shoulder massage and a manicure" style="left:0;top:0;width:380px;height:380px;background:linear-gradient(160deg,#c99a7a 0%,#e8cdb9 55%,#f4e6dd 100%);"></div>
    <svg class="layer" viewBox="0 0 380 820" aria-hidden="true">
      <path d="M0 330 Q190 380 380 300 V820 H0 Z" fill="var(--blush)"/>
      <path d="M0 350 Q190 400 380 320 V820 H0 Z" fill="var(--plum)"/>
    </svg>
    <div class="service service--light" style="top:410px;left:40px">
      <span class="pill pill--on-plum">Manicure &amp; Pédicure</span>
      <ul class="service__list">
        <li>Semi permanent</li>
        <li>Gel</li>
        <li>Fibre de verre</li>
      </ul>
    </div>
    <div class="service service--light" style="top:600px;left:40px">
      <span class="pill pill--on-plum">Spa des pieds</span>
      <ul class="service__list">
        <li>Argile thérapie</li>
        <li>Paraffine</li>
        <li>Plasma</li>
      </ul>
    </div>
  </article>
</section>

</body>
</html>
```